Flier needed for parenting seminar

Hello! We need a 4 by 6 clubcard needed for an upcoming parenting seminar. Flier should be in color, good quality images, and be front/back.
We are looking for something fresh, eye-catching, and not generic. Thanks!
CLUBCARD FRONT:
Veltran Institute presents:
Hearthbound Parenting:
Growing Steadfast Homes
By Shaykh Idris Kamal Tarbusi
Sat & Sun
Oct 22 & 23, 2016
9am - 7pm
Location: ORB Samira Hall
4187 Marlow Blvd
Santa Clara, CA 95127
Seating is limited. Register now!
Www.VeltranInstitute.com
1-877-Veltra7
CLUBCARD BACK:
There are no guarantees in life as to raising children to be how they should. Indeed, even Noah (as) lost his son while the Pharaoh's wife was able to raise Moses (as). And while traditionally a woman rears the child, Zakariyah (as) was a man chosen to raise one. The variety of scenarios in the Quran cover all possibilities. It is therefore worth reflecting on them to gain insight and draw parenting lessons.
So come and explore the Quranic view and prophetic guidelines for raising children. We hope this course serves as a landmark for you to know best practices and tools available to you, rooted in Quranic wisdom as well as our own experiences.
Some topics:
- The ways of Quranic raising
- Tools & examples from The Book
- What not to do
- Truth vs wisdom
www.VeltranInstitute.com
1-877-Veltra7
Parents, ppl considering becoming parents, ppl studying child development
- Fresh
- Eye-catching, not generic.
- Silhouette of mother/father with a young child.
- Maybe even praying together...

```html
<!DOCTYPE html>
<html lang="en">
<head>
<meta charset="utf-8">
<title>Veltran Institute – Parenting Seminar Clubcard</title>
<link href="https://fonts.googleapis.com/css2?family=Arimo:ital,wght@0,400;0,700;1,400&family=Baloo+2:wght@800&family=Cormorant+Garamond:ital,wght@1,600&display=swap" rel="stylesheet">
<style>
  :root {
    --stage: #1c5a8a;
    --navy: #26256c;
    --title: #2b2a74;
    --sky: #1ba4ea;
    --sky-deep: #1b7fd6;
    --lilac-top: #a59ed3;
    --lilac-mid: #dcd8f0;
    --ice: #bfe5f0;
    --ice-light: #eaf6fa;
    --ink: #1e1e1e;
    --white: #ffffff;
  }
  * { box-sizing: border-box; margin: 0; padding: 0; }
  html, body { width: 1200px; height: 1200px; overflow: hidden; }
  body {
    background: var(--stage);
    font-family: "Arimo", Arial, sans-serif;
    position: relative;
  }
  .card {
    position: absolute;
    top: 180px;
    width: 560px;
    height: 840px;
    background: var(--white);
    overflow: hidden;
  }
  .card--front { left: 30px; }
  .card--back { left: 610px; }

  /* FRONT */
  .front-sky {
    position: absolute; left: 0; top: 0; width: 100%; height: 420px;
    background: radial-gradient(ellipse at 50% 22%, var(--white) 0%, var(--lilac-mid) 45%, var(--lilac-top) 100%);
  }
  .brand {
    position: absolute; top: 58px; left: 0; width: 100%;
    text-align: center;
    font-family: "Cormorant Garamond", Georgia, serif;
    font-style: italic; font-weight: 600;
    font-size: 40px; color: var(--title);
    letter-spacing: 1px;
  }
  .front-photo {
    position: absolute; left: 0; top: 215px; width: 100%; height: 200px;
    background: linear-gradient(180deg, #cfc7e6 0%, #e8c9d2 55%, #b9d5ec 100%);
  }
  .front-white {
    position: absolute; left: 0; top: 392px; width: 100%; height: 370px;
    background: var(--white);
    clip-path: polygon(0 4%, 100% 0, 100% 100%, 0 100%);
  }
  .seminar-tag {
    position: absolute; top: 382px; left: 0; width: 100%;
    text-align: center;
    font-family: "Baloo 2", "Arial Rounded MT Bold", sans-serif;
    font-weight: 800; font-size: 33px; color: var(--sky);
  }
  .title {
    position: absolute; top: 446px; left: 0; width: 100%;
    text-align: center;
    font-weight: 700; font-size: 47px; line-height: 53px;
    color: var(--title);
  }
  .byline {
    position: absolute; top: 566px; left: 0; width: 100%;
    text-align: center; font-style: italic; font-size: 23px; color: var(--title);
  }
  .ribbon { position: absolute; left: 100px; top: 610px; width: 350px; height: 120px; }
  .ribbon-text {
    position: absolute; left: 110px; top: 633px; width: 290px;
    text-align: center; font-weight: 700; font-size: 21px; line-height: 24px;
    color: var(--navy);
  }
  .front-accent { position: absolute; left: 0; top: 700px; width: 560px; height: 60px; }
  .front-band {
    position: absolute; left: 0; bottom: 0; width: 100%; height: 86px;
    background: var(--navy);
    color: var(--white); text-align: center;
    font-size: 19px; line-height: 24px; padding-top: 11px;
  }

  /* BACK */
  .intro {
    position: absolute; left: 39px; right: 36px; top: 44px;
    font-size: 16.4px; line-height: 20.3px; color: var(--ink);
    text-align: justify; letter-spacing: -0.1px;
  }
  .intro p + p { margin-top: 16px; }
  .topics-panel {
    position: absolute; left: 0; top: 302px; width: 100%; height: 408px;
    background: linear-gradient(160deg, var(--ice) 0%, var(--ice-light) 100%);
  }
  .topics-heading {
    position: absolute; left: 39px; top: 312px;
    font-weight: 700; font-size: 27px; color: var(--title);
  }
  .topics-list {
    position: absolute; left: 39px; top: 354px; list-style: none;
    font-size: 18.5px; color: var(--ink);
  }
  .topics-list li { height: 29px; display: flex; align-items: center; }
  .topics-list li::before {
    content: ""; width: 9px; height: 9px; background: var(--ink);
    margin-right: 13px; flex: none;
  }
  .back-photo {
    position: absolute; left: 155px; top: 440px; width: 400px; height: 270px;
    background: linear-gradient(180deg, #d7eef5 0%, #f0e2c4 50%, #e9a7a6 100%);
    border-radius: 120px 120px 0 0;
  }
  .back-band {
    position: absolute; left: 0; bottom: 0; width: 100%; height: 130px;
    background: var(--navy);
    border-top: 6px solid var(--sky-deep);
    color: var(--white); text-align: center; padding-top: 14px;
  }
  .cta { font-weight: 700; font-size: 22px; margin-bottom: 7px; }
  .contact { font-size: 19px; line-height: 27px; }
</style>
</head>
<body>

<section class="card card--front">
  <div class="front-sky"></div>
  <div class="brand">Veltran Institute</div>
  <div class="front-photo" role="img" aria-label="Photo of a smiling family of four lying together: father, mother, son and daughter"></div>
  <div class="front-white"></div>
  <div class="seminar-tag">Parenting Seminar</div>
  <h1 class="title">GROWING STEADFAST<br>HOMES</h1>
  <p class="byline">By Shaykh Idris Kamal Tarbusi</p>

  <svg class="ribbon" viewBox="0 0 350 120" aria-hidden="true">
    <defs>
      <linearGradient id="ribbonFill" x1="0" x2="1" y1="0" y2="0">
        <stop offset="0" stop-color="#2bb3ee"/>
        <stop offset="1" stop-color="#1a9be6"/>
      </linearGradient>
    </defs>
    <polygon points="300,2 330,22 270,24" fill="#6a78c8"/>
    <polygon points="12,112 75,104 75,120" fill="#8a90d0"/>
    <polygon points="0,18 340,24 300,104 15,104" fill="url(#ribbonFill)"/>
  </svg>
  <div class="ribbon-text">Sat &amp; Sun<br>Oct 22 &amp; 23, 2016<br>9am - 7pm</div>

  <svg class="front-accent" viewBox="0 0 560 60" aria-hidden="true">
    <polygon points="520,54 560,14 560,22 526,58" fill="#1b7fd6"/>
    <rect x="0" y="52" width="525" height="4" fill="#1b7fd6"/>
  </svg>

  <div class="front-band">
    Location : ORB Samira Hall<br>
    4187 Marlow Blvd, Santa Clara, CA 95127
  </div>
</section>

<section class="card card--back">
  <div class="intro">
    <p>There are no guarantees in life as to raising children to be how they should. Indeed, even Noah (as) lost his son while the Pharaoh's wife was able to raise Moses (as). And while traditionally a woman rears the child, Zakariyah (as) was a man chosen to raise one. The variety of scenarios in the Quran cover all possibilities. It is therefore worth reflecting on them to gain insight and draw parenting lessons.</p>
    <p>So come and explore the Quranic view and prophetic guidelines for raising children. We hope this course serves as a landmark for you to know best practices and tools available to you, rooted in Quranic wisdom as well as our own experiences.</p>
  </div>

  <div class="topics-panel"></div>
  <h2 class="topics-heading">Some Topics</h2>
  <ul class="topics-list">
    <li>The ways of Quranic raising</li>
    <li>Tools &amp; examples from The Book</li>
    <li>What not to do</li>
    <li>Truth vs wisdom</li>
  </ul>
  <div class="back-photo" role="img" aria-label="Photo of a happy family embracing: mother, father, son and daughter"></div>

  <div class="back-band">
    <p class="cta">Seating is limited. Register now!</p>
    <p class="contact">www.VeltranInstitute.com<br>1-877-Veltra7</p>
  </div>
</section>

</body>
</html>
```